Shop front signage design for Bubble Tea Shop

Tapioca Grove is Sydney based Green Tea Shop.We are looking for a modern and sleek signage for shop front end. We have Aluminium Composite Panel and Awning sign at the shop front. We will keep Aluminium composite panel simple with logo and text. We are after awning design which is above glass door and under the panel. Old Awning is PVC foam in two pieces 2310mm w x 1000mm h. We need someone to design awing. It should reflect Bubble tea and using bubble tea cups with pearls is essential. Stock images can be used. Avoid using icons or illustrative icons as we are after real images of bubble tea cup. This is to ensure that the brand is not taken as juice shop or cafe.
Panel Dimensions is 5250 mm w x 580 mm h.Awning/ Fascia sign is 4720 mm w x 1000 mm h.
Logo and signage concept is attached.

Target Market(s)

Corporate Male and Female, school, general public.

Colors
f36e22
333333
000000
eaeaea
cbcbcb

Requirements
Must have
• Bubble tea cups with fruit or milk tea.
Should not have
• Icons, illustration

```html
<!DOCTYPE html>
<html lang="en">
<head>
<meta charset="utf-8">
<title>Tapioca Grove – Shop Front Signage</title>
<link rel="stylesheet" href="https://fonts.googleapis.com/css2?family=Nunito:wght@800&family=Fjalla+One&family=Montserrat:wght@600&family=Lobster&family=Roboto:wght@500&display=swap">
<style>
  :root {
    --brand-orange: #f36e22;
    --ink: #000000;
    --charcoal: #333333;
    --mist: #eaeaea;
    --silver: #cbcbcb;
    --paper: #ffffff;
  }
  * { margin: 0; padding: 0; box-sizing: border-box; }
  html, body {
    width: 1200px; height: 750px; overflow: hidden;
    background: var(--mist);
  }
  .canvas { position: relative; width: 1200px; height: 750px; }

  .sign {
    position: absolute; left: 40px; width: 1120px; height: 236px;
    background: var(--paper); overflow: hidden;
  }
  .sign--panel { top: 120px; }
  .sign--awning { top: 420px; }

  .sign__shape { position: absolute; inset: 0; }

  .brand {
    position: absolute; display: flex; align-items: center; gap: 14px;
    font-family: "Nunito", sans-serif; font-weight: 800; font-size: 42px;
    letter-spacing: -0.5px;
  }
  .brand__dot { width: 64px; height: 64px; border-radius: 50%; flex: none; }
  .sign--panel .brand { left: 48px; top: 86px; color: var(--paper); }
  .sign--panel .brand__dot { border: 5px solid var(--paper); }
  .sign--awning .brand { left: 34px; top: 74px; color: var(--ink); }
  .sign--awning .brand__dot { width: 52px; height: 52px; background: var(--ink); }

  .product-photo { position: absolute; border-radius: 6px; }
  .sign--panel .product-photo {
    left: 570px; top: 18px; width: 350px; height: 170px;
    background: linear-gradient(90deg, #e8e6f2 0%, #f6c9dc 22%, #f4efb4 45%, #b9ebc8 68%, #efc79a 90%);
  }
  .sign--awning .product-photo {
    left: 500px; top: 22px; width: 370px; height: 170px;
    background: linear-gradient(90deg, #e6e4ef 0%, #f3c7d8 22%, #f2eeb6 45%, #b8e9c6 68%, #edcca8 90%);
  }

  .tagline { position: absolute; right: 34px; text-align: right; line-height: 1; }
  .tagline__script {
    display: block; font-family: "Lobster", cursive; font-size: 64px;
    color: var(--brand-orange); transform: rotate(-6deg); transform-origin: right;
  }
  .tagline__word {
    display: block; font-family: "Roboto", sans-serif; font-weight: 500;
    font-size: 36px; color: var(--ink); margin-top: 2px;
  }
  .sign--panel .tagline { top: 42px; }
  .sign--awning .tagline { top: 52px; }

  .menu-line {
    position: absolute; left: 584px; top: 196px; display: flex; gap: 16px;
    font-family: "Fjalla One", sans-serif; font-size: 24px; color: var(--ink);
  }
  .menu-line__sep { color: var(--charcoal); }

  .menu-band {
    position: absolute; left: 0; right: 0; bottom: 0; height: 46px;
    background: var(--brand-orange); display: flex; align-items: center;
    padding-left: 102px; gap: 40px;
    font-family: "Montserrat", sans-serif; font-weight: 600; font-size: 23px;
    letter-spacing: 3.5px; color: var(--paper);
  }
  .menu-band__sep { width: 2px; height: 22px; background: var(--paper); }
</style>
</head>
<body>
<main class="canvas">

  <section class="sign sign--panel" aria-label="Aluminium composite panel">
    <svg class="sign__shape" viewBox="0 0 1120 236" aria-hidden="true">
      <path d="M0 0 H470 C480 90 510 175 540 236 H0 Z" fill="var(--brand-orange)"/>
      <path d="M488 0 C490 90 518 175 556 236" fill="none" stroke="var(--brand-orange)" stroke-width="3"/>
    </svg>
    <div class="brand"><span class="brand__dot"></span>Tapioca Grove</div>
    <div class="product-photo" role="img" aria-label="Photo of five bubble tea cups with domed lids, straws and tapioca pearls in milk, pink, yellow, green and brown"></div>
    <div class="tagline">
      <span class="tagline__script">Fresh</span>
      <span class="tagline__word">Juice</span>
    </div>
    <div class="menu-line">
      <span>Pearl Tea</span><span class="menu-line__sep">|</span>
      <span>Fruit Tea</span><span class="menu-line__sep">|</span>
      <span>Green Tea</span><span class="menu-line__sep">|</span>
      <span>Ice Frappe</span>
    </div>
  </section>

  <section class="sign sign--awning" aria-label="Awning sign">
    <div class="brand"><span class="brand__dot"></span>Tapioca Grove</div>
    <div class="product-photo" role="img" aria-label="Photo of five bubble tea cups with pearls surrounded by fresh fruit, berries, kiwi, passionfruit and chocolate"></div>
    <div class="tagline">
      <span class="tagline__script">Bubble</span>
      <span class="tagline__word">Tea</span>
    </div>
    <div class="menu-band">
      <span>PEARL TEA</span><span class="menu-band__sep"></span>
      <span>FRUIT TEA</span><span class="menu-band__sep"></span>
      <span>GREEN TEA</span><span class="menu-band__sep"></span>
      <span>ICE FRAPPE</span>
    </div>
  </section>

</main>
</body>
</html>
```